International Hand & Body company needing a Hand cream tube design for the Retail market

I am wanting a modern design for a new range of 6 hand creams I will be launching in August. They need to compliment our range of wrapped soaps which you can see on www.plomvane.com.au so am wanting clean designs. I am wanting a solid colour with a hand drawn organic feel line drawing in black elegantly placed wrapping around the label. I am wanting to focus on the colour and positioning of words and fonts. I like modern clean contemporary fonts. The final design needs to appeal to the broader female market.This may lead to range expansion if designs are well received.
Updates

These designs are not hitting the brief. They are too generic and look like a supermarket brand. Our brand is more boutique and this design needs to be modern and simple. I would like more solid colours and more modern designs. Without patterns.

Target Market(s)

Female aged 20 - 70

Requirements
Must have
• a modern contemporary design that will appeal to the masses.
• Please read attached brief.
Should not have
• a black botanical illustration, in a loose and organic design to match the fragrance.

```html
<!DOCTYPE html>
<html lang="en">
<head>
<meta charset="utf-8">
<title>Plomvane Hand Cream – Tube Labels</title>
<link rel="stylesheet" href="https://fonts.googleapis.com/css2?family=Montserrat:wght@400;500;600;800&display=swap">
<style>
  :root {
    --magenta: #e8177f;
    --gold: #fbb017;
    --orange: #f37b21;
    --blue: #00a9d0;
    --teal: #00b39a;
    --ink: #111111;
    --paper: #ffffff;
    --fold: rgba(255,255,255,0.55);
  }
  * { box-sizing: border-box; margin: 0; padding: 0; }
  html, body { width: 1200px; height: 428px; overflow: hidden; background: var(--paper); }
  body { position: relative; font-family: "Montserrat", Arial, sans-serif; color: var(--ink); }

  .sheet-title { position: absolute; left: 63px; top: 46px; font-size: 7px; font-weight: 800; letter-spacing: 0.02em; }

  .tube { position: absolute; top: 66px; width: 111px; height: 303px; background: var(--bg); }
  .tube--spread { left: 63px; width: 222px; }
  .tube::before, .tube::after { content: ""; position: absolute; left: 0; right: 0; border-top: 1px dashed var(--fold); }
  .tube::before { top: 18px; }
  .tube::after { bottom: 17px; }
  .fold-line { position: absolute; left: 111px; top: 0; height: 63px; border-left: 1px dashed var(--fold); }

  .label { position: absolute; left: 25px; right: 0; top: 63px; height: 189px; background: var(--face); overflow: hidden; }
  .frame { position: absolute; left: 5px; top: 5px; right: -10px; bottom: 5px; border: 4px solid var(--ink); }

  .front { position: absolute; left: 15px; top: 0; width: 62px; }
  .brand { position: absolute; top: 20px; left: 0; font-size: 9.5px; font-weight: 500; letter-spacing: 0.03em; white-space: nowrap; }
  .rule { position: absolute; left: 0; width: 55px; border-top: 1px solid var(--ink); }
  .rule--a { top: 67px; } .rule--b { top: 111px; } .rule--c { top: 124px; }
  .flavour { position: absolute; left: 0; top: 74px; font-size: 10.5px; font-weight: 800; line-height: 11px; text-transform: uppercase; white-space: nowrap; }
  .flavour--three { top: 69px; }
  .product { position: absolute; left: 0; top: 115px; font-size: 6px; font-weight: 500; letter-spacing: 0.04em; white-space: nowrap; }
  .descriptor { position: absolute; left: 0; top: 132px; width: 64px; font-size: 2.9px; line-height: 3.8px; font-weight: 500; }
  .origin { position: absolute; left: 0; top: 156px; font-size: 3.6px; font-weight: 800; white-space: nowrap; }
  .volume { position: absolute; left: 0; top: 162px; font-size: 4.6px; font-weight: 600; white-space: nowrap; }

  .back { position: absolute; left: 102px; top: 0; width: 92px; font-size: 2.7px; line-height: 3.5px; font-weight: 500; }
  .back .brand { left: 0; }
  .claims { position: absolute; top: 46px; left: 0; font-weight: 800; }
  .ingredients { position: absolute; top: 70px; left: 0; width: 90px; }
  .warning { position: absolute; top: 101px; left: 0; width: 90px; }
  .usage { position: absolute; top: 112px; left: 0; width: 90px; }
  .suits { position: absolute; top: 120px; left: 0; font-size: 4.4px; font-weight: 800; white-space: nowrap; }
  .marks { position: absolute; top: 128px; left: 0; display: flex; gap: 2.5px; }
  .marks span { width: 8px; height: 8px; background: var(--ink); }
  .marks span.round { border-radius: 50%; }
  .address { position: absolute; top: 131px; left: 52px; font-size: 2.5px; width: 40px; }
  .contact { position: absolute; top: 147px; left: 0; font-size: 3.4px; font-weight: 600; white-space: nowrap; }
  .batch { position: absolute; top: 150px; left: 92px; font-size: 2.6px; transform: rotate(-90deg); transform-origin: left top; white-space: nowrap; }
</style>
</head>
<body>
  <div class="sheet-title">FRONT AND BACK</div>

  <!-- Fig & Sandalwood spread -->
  <div class="tube tube--spread" style="--bg: var(--magenta); --face: var(--gold);">
    <div class="fold-line"></div>
    <div class="label">
      <div class="frame"></div>
      <div class="front">
        <div class="brand">plomvane</div>
        <div class="rule rule--a"></div>
        <div class="flavour flavour--three">Fig &amp;<br>Sandal<br>Wood</div>
        <div class="rule rule--b"></div>
        <div class="product">HAND CREAM</div>
        <div class="rule rule--c"></div>
        <div class="descriptor">NOURISHING NON-GREASY CREAM TO<br>KEEP SKIN SOFT &amp; HYDRATED</div>
        <div class="origin">MADE IN AUSTRALIA</div>
        <div class="volume">35mL ℮ 1.18 fl. oz.</div>
      </div>
      <div class="back">
        <div class="brand">plomvane</div>
        <div class="claims">NO MINERAL OILS<br>NO ARTIFICIAL COLOURS<br>NO SILICONES<br>NO PARABENS</div>
        <div class="ingredients"><b>INGREDIENTS:</b> AQUA, SHEA BUTTER, GLYCERIN, SWEET ALMOND OIL, CETEARYL ALCOHOL, COCONUT OIL, FIG EXTRACT, SANDALWOOD OIL, VITAMIN E, XANTHAN GUM, ALOE VERA, JOJOBA OIL, FRAGRANCE, LINALOOL, LIMONENE.</div>
        <div class="warning"><b>WARNING:</b> FOR EXTERNAL USE ONLY. AVOID CONTACT WITH EYES. STOP USE IF IRRITATION OCCURS.</div>
        <div class="usage"><b>USAGE:</b> MASSAGE INTO CLEAN HANDS AS NEEDED.</div>
        <div class="suits">SUITABLE FOR ALL SKIN TYPES</div>
        <div class="marks" role="img" aria-label="Social and certification marks">
          <span></span><span></span><span class="round"></span><span></span>
        </div>
        <div class="address">Unit 4 / 22 Harbour Street Fremantle WA 6160</div>
        <div class="contact">www.plomvane.com.au &nbsp;|&nbsp; sales@plomvane.com.au</div>
        <div class="batch">Code: HC01</div>
      </div>
    </div>
  </div>

  <!-- Fig & Sandalwood front -->
  <div class="tube" style="left:345px; --bg: var(--magenta); --face: var(--gold);">
    <div class="label"><div class="frame"></div>
      <div class="front">
        <div class="brand">plomvane</div><div class="rule rule--a"></div>
        <div class="flavour flavour--three">Fig &amp;<br>Sandal<br>Wood</div>
        <div class="rule rule--b"></div><div class="product">HAND CREAM</div><div class="rule rule--c"></div>
        <div class="descriptor">NOURISHING NON-GREASY CREAM TO<br>KEEP SKIN SOFT &amp; HYDRATED</div>
        <div class="origin">MADE IN AUSTRALIA</div><div class="volume">35mL ℮ 1.18 fl. oz.</div>
      </div>
    </div>
  </div>

  <!-- Citrus & Seagrass -->
  <div class="tube" style="left:476px; --bg: var(--orange); --face: var(--teal);">
    <div class="label"><div class="frame"></div>
      <div class="front">
        <div class="brand">plomvane</div><div class="rule rule--a"></div>
        <div class="flavour">Citrus &amp;<br>Seagrass</div>
        <div class="rule rule--b"></div><div class="product">HAND CREAM</div><div class="rule rule--c"></div>
        <div class="descriptor">NOURISHING NON-GREASY CREAM TO<br>KEEP SKIN SOFT &amp; HYDRATED</div>
        <div class="origin">MADE IN AUSTRALIA</div><div class="volume">35mL ℮ 1.18 fl. oz.</div>
      </div>
    </div>
  </div>

  <!-- Yuzu & Sage – orange -->
  <div class="tube" style="left:608px; --bg: var(--blue); --face: var(--orange);">
    <div class="label"><div class="frame"></div>
      <div class="front">
        <div class="brand">plomvane</div><div class="rule rule--a"></div>
        <div class="flavour">Yuzu &amp;<br>Sage</div>
        <div class="rule rule--b"></div><div class="product">HAND CREAM</div><div class="rule rule--c"></div>
        <div class="descriptor">NOURISHING NON-GREASY CREAM TO<br>KEEP SKIN SOFT &amp; HYDRATED</div>
        <div class="origin">MADE IN AUSTRALIA</div><div class="volume">35mL ℮ 1.18 fl. oz.</div>
      </div>
    </div>
  </div>

  <!-- Yuzu & Sage – magenta -->
  <div class="tube" style="left:740px; --bg: var(--teal); --face: var(--magenta);">
    <div class="label"><div class="frame"></div>
      <div class="front">
        <div class="brand">plomvane</div><div class="rule rule--a"></div>
        <div class="flavour">Yuzu &amp;<br>Sage</div>
        <div class="rule rule--b"></div><div class="product">HAND CREAM</div><div class="rule rule--c"></div>
        <div class="descriptor">NOURISHING NON-GREASY CREAM TO<br>KEEP SKIN SOFT &amp; HYDRATED</div>
        <div class="origin">MADE IN AUSTRALIA</div><div class="volume">35mL ℮ 1.18 fl. oz.</div>
      </div>
    </div>
  </div>

  <!-- Yuzu & Sage – blue -->
  <div class="tube" style="left:872px; --bg: var(--magenta); --face: var(--blue);">
    <div class="label"><div class="frame"></div>
      <div class="front">
        <div class="brand">plomvane</div><div class="rule rule--a"></div>
        <div class="flavour">Yuzu &amp;<br>Sage</div>
        <div class="rule rule--b"></div><div class="product">HAND CREAM</div><div class="rule rule--c"></div>
        <div class="descriptor">NOURISHING NON-GREASY CREAM TO<br>KEEP SKIN SOFT &amp; HYDRATED</div>
        <div class="origin">MADE IN AUSTRALIA</div><div class="volume">35mL ℮ 1.18 fl. oz.</div>
      </div>
    </div>
  </div>

  <!-- Yuzu & Sage – teal -->
  <div class="tube" style="left:1003px; top:61px; --bg: var(--gold); --face: var(--teal);">
    <div class="label"><div class="frame"></div>
      <div class="front">
        <div class="brand">plomvane</div><div class="rule rule--a"></div>
        <div class="flavour">Yuzu &amp;<br>Sage</div>
        <div class="rule rule--b"></div><div class="product">HAND CREAM</div><div class="rule rule--c"></div>
        <div class="descriptor">NOURISHING NON-GREASY CREAM TO<br>KEEP SKIN SOFT &amp; HYDRATED</div>
        <div class="origin">MADE IN AUSTRALIA</div><div class="volume">35mL ℮ 1.18 fl. oz.</div>
      </div>
    </div>
  </div>
</body>
</html>
```